Teams Background for client video calls - giving them a feel who we are

I'm keen to create a background artwork of a modern dynamic office that also reflects our values which are all about transparency, humility, integrity etc. Our company is called Corvelle Bridging. Our behaviours are agility, excellence and precision. You can find all about our colours and branding under our website www.corvellebridging.com

Target Market(s)

IT Recruitment

Industry/Entity Type

IT Recruitment

Other font styles liked:
• as per our website www.corvellebridging.com

Colors
0054AA
0677BA
7BADD7
CADEEF
E8F1F8

Requirements
Must have
• A modern cool dynamic work office design incooperating our logo and what we stand for in terms of colours and our values and behaviours we live as a company. As i founded the office in the cabin but now we are in a modern office a blend would work i think.

```html
<!DOCTYPE html>
<html lang="en">
<head>
<meta charset="utf-8">
<title>Corvelle Bridging – Call Background</title>
<link rel="stylesheet" href="https://fonts.googleapis.com/css2?family=Oswald:wght@300;600&display=swap">
<style>
  :root {
    --white: #ffffff;
    --teal: #00a696;
    --teal-mid: #14a6c2;
    --sky: #2fa9e0;
    --royal: #0a84d6;
    --ice: #c6f1fa;
    --pale: #bfe6fb;
    --dot-blue: #2a9ee0;
  }
  * { margin: 0; padding: 0; box-sizing: border-box; }
  html, body { width: 1200px; height: 675px; overflow: hidden; background: var(--white); }
  .call-background {
    position: relative;
    width: 1200px;
    height: 675px;
    overflow: hidden;
    font-family: "Oswald", "Arial Narrow", sans-serif;
    background:
      radial-gradient(ellipse 420px 360px at 60px 40px, var(--white) 0%, rgba(255,255,255,0.9) 40%, rgba(255,255,255,0) 100%),
      radial-gradient(ellipse 520px 380px at 1200px 0px, var(--teal) 0%, rgba(0,166,150,0.6) 45%, rgba(0,166,150,0) 100%),
      radial-gradient(ellipse 460px 320px at 0px 675px, var(--royal) 0%, rgba(10,132,214,0.7) 40%, rgba(10,132,214,0) 100%),
      radial-gradient(ellipse 420px 300px at 1200px 675px, var(--pale) 0%, rgba(191,230,251,0) 100%),
      radial-gradient(ellipse 500px 360px at 480px 520px, var(--ice) 0%, rgba(198,241,250,0) 100%),
      linear-gradient(135deg, #f4fcfe 0%, #8fd8ee 35%, var(--sky) 60%, #7fcdf4 100%);
  }
  .light-arcs { position: absolute; inset: 0; width: 100%; height: 100%; }
  .dot-grid { position: absolute; display: grid; grid-template-columns: repeat(4, 8px); gap: 11px; }
  .dot-grid span { width: 8px; height: 8px; border-radius: 50%; }
  .dot-grid--top { left: 59px; top: 75px; }
  .dot-grid--top span { background: var(--dot-blue); }
  .dot-grid--bottom { left: 1076px; top: 577px; }
  .dot-grid--bottom span { background: var(--white); }
  .brand-name {
    position: absolute;
    right: 64px;
    top: 58px;
    display: flex;
    align-items: center;
    gap: 12px;
    color: var(--white);
    font-weight: 600;
    font-size: 30px;
    letter-spacing: 0.5px;
  }
  .brand-name .brand-dot { width: 14px; height: 14px; border-radius: 50%; background: var(--white); }
  .values {
    position: absolute;
    left: 67px;
    top: 449px;
    color: var(--white);
    font-size: 42px;
    line-height: 42px;
    text-transform: uppercase;
    letter-spacing: -0.5px;
  }
  .values .value { font-weight: 300; }
  .values .value--strong { font-weight: 600; }
</style>
</head>
<body>
<main class="call-background">
  <svg class="light-arcs" viewBox="0 0 1200 675" aria-hidden="true">
    <defs>
      <filter id="soft-glow" x="-20%" y="-20%" width="140%" height="140%">
        <feGaussianBlur stdDeviation="14"/>
      </filter>
    </defs>
    <g fill="none" stroke="#ffffff" stroke-width="30" filter="url(#soft-glow)" opacity="0.85">
      <circle cx="590" cy="-90" r="390"/>
      <circle cx="1215" cy="690" r="450"/>
      <circle cx="190" cy="730" r="440"/>
    </g>
  </svg>

  <div class="dot-grid dot-grid--top" aria-hidden="true">
    <span></span><span></span><span></span><span></span>
    <span></span><span></span><span></span><span></span>
    <span></span><span></span><span></span><span></span>
    <span></span><span></span><span></span><span></span>
  </div>

  <div class="brand-name"><span class="brand-dot"></span>Corvelle Bridging</div>

  <div class="values">
    <div><span class="value">Transparency</span></div>
    <div><span class="value--strong">Humility</span> <span class="value">Integrity</span></div>
    <div><span class="value">Excellence</span> <span class="value--strong">Agility</span></div>
    <div><span class="value--strong">Precision</span></div>
  </div>

  <div class="dot-grid dot-grid--bottom" aria-hidden="true">
    <span></span><span></span><span></span><span></span>
    <span></span><span></span><span></span><span></span>
    <span></span><span></span><span></span><span></span>
    <span></span><span></span><span></span><span></span>
  </div>
</main>
</body>
</html>
```